Thank You Card

I'm looking for a thank you card design using our logo and other graphics. We are an essential business and our employees (Electricians) have done an incredible job staying healthy and safe during the COVID-19 pandemic, I want to send each a thank you card.

```html
<!DOCTYPE html>
<html lang="en">
<head>
<meta charset="utf-8">
<title>Thank You Card – Front and Back</title>
<link rel="stylesheet" href="https://fonts.googleapis.com/css2?family=Courgette&family=Montserrat:wght@400&family=Open+Sans:wght@400;700&display=swap">
<style>
  :root {
    --page-bg: #ffffff;
    --card-core: #2b2a68;
    --card-mid: #17162f;
    --card-edge: #000000;
    --neon: #dff6ff;
    --neon-glow: #3fb8f0;
    --text-light: #ffffff;
    --label-ink: #111111;
    --brand-red: #d3232a;
    --band-red: #c9222a;
    --logo-bg: #ffffff;
  }
  * { margin: 0; padding: 0; box-sizing: border-box; }
  html, body { width: 1200px; height: 1200px; overflow: hidden; background: var(--page-bg); }
  .sheet { position: relative; width: 1200px; height: 1200px; }

  .card {
    position: absolute;
    overflow: hidden;
    box-shadow: 0 6px 16px rgba(0,0,0,0.35);
    font-family: 'Open Sans', sans-serif;
    color: var(--text-light);
  }
  .card--front { left: 56px; top: 29px; width: 794px; height: 536px; }
  .card--back  { left: 374px; top: 621px; width: 786px; height: 531px; }

  .card__backdrop {
    position: absolute; inset: 0;
    background: radial-gradient(ellipse 62% 68% at 50% 48%, var(--card-core) 0%, var(--card-mid) 60%, var(--card-edge) 100%);
  }

  .brand-box {
    position: absolute;
    width: 250px; height: 115px;
    background: var(--logo-bg);
    display: flex; flex-direction: column; align-items: center; justify-content: center;
    color: var(--brand-red);
    font-family: 'Open Sans', sans-serif;
    font-weight: 700;
    line-height: 1.05;
    text-align: center;
  }
  .brand-box__main { font-size: 31px; letter-spacing: 0.5px; }
  .brand-box__sub { font-size: 17px; letter-spacing: 1.5px; margin-top: 4px; }
  .card--front .brand-box { left: 270px; top: 50px; }
  .card--back .brand-box { left: 269px; top: 49px; }

  .headline {
    position: absolute; left: 0; right: 0; top: 222px;
    text-align: center;
    font-family: 'Montserrat', sans-serif;
    font-weight: 400;
    font-size: 101px;
    letter-spacing: 4px;
    line-height: 1;
    color: var(--neon);
    text-shadow: 0 0 6px var(--neon-glow), 0 0 14px var(--neon-glow), 0 0 26px rgba(63,184,240,0.7);
  }
  .subline {
    position: absolute; left: 0; right: 0; top: 334px;
    text-align: center;
    font-size: 21px;
    letter-spacing: -0.2px;
  }

  .message {
    position: absolute; left: 40px; right: 40px; top: 202px;
    text-align: center;
    font-family: 'Courgette', cursive;
    font-size: 27px;
    line-height: 33px;
  }
  .stay-safe {
    position: absolute; left: 100px; top: 339px;
    width: 587px; height: 57px;
    background: var(--band-red);
    display: flex; align-items: center; justify-content: center;
    font-family: 'Courgette', cursive;
    font-size: 32px;
    letter-spacing: 0.5px;
  }
  .web {
    position: absolute; left: 0; right: 0; top: 465px;
    text-align: center;
    font-size: 21px;
  }

  .side-label {
    position: absolute;
    font-family: 'Open Sans', sans-serif;
    font-size: 25px;
    color: var(--label-ink);
  }
  .side-label--front { left: 888px; top: 278px; }
  .side-label--back { left: 214px; top: 832px; }
</style>
</head>
<body>
<div class="sheet">

  <section class="card card--front" aria-label="Card front">
    <div class="card__backdrop" role="img" aria-label="Dark navy background with decorative diagonal neon light streaks in blue, violet and orange"></div>
    <div class="brand-box">
      <span class="brand-box__main">BRIGHTLINE</span>
      <span class="brand-box__sub">ELECTRIC SERVICES</span>
    </div>
    <h1 class="headline">THANK YOU</h1>
    <p class="subline">FOR GIVING 100% DURING THIS COVID-19 PANDEMIC</p>
  </section>
  <p class="side-label side-label--front">FRONT PAGE</p>

  <section class="card card--back" aria-label="Card back">
    <div class="card__backdrop" role="img" aria-label="Dark navy background with decorative diagonal neon light streaks in blue, violet and orange"></div>
    <div class="brand-box">
      <span class="brand-box__main">BRIGHTLINE</span>
      <span class="brand-box__sub">ELECTRIC SERVICES</span>
    </div>
    <p class="message">Thank you for all your efforts and dedication.<br>Your sincere service needs all our encouragement<br>and appreciation.</p>
    <p class="stay-safe">We are with You. Please Stay Safe</p>
    <p class="web">www.brightlineelectric.com</p>
  </section>
  <p class="side-label side-label--back">BACK PAGE</p>

</div>
</body>
</html>
```